International Wine events organiser seeks simple but stunning business card

I am a freelance events, marketing and PR provider specialised in the Wine industry. I help wineries and wine regions reach trade and consumers in foreign markets through events, help with the websites and communications, press trips and promotional activities. I am looking for a business card which is simple yet effective and is linked to events and communication.

I work mainly - but exclusively - with Italian wineries organising events for them in foreign market.s

I would like to use red in the logo as my present website (lunabrendor.com) used grey and red (although I will be changing the design at a later date).

Target Market(s)

Wine producers, promotional bodies in wine sector, companies looking to hire event organisers,

Industry/Entity Type

Marketing

Requirements
Must have
• My Name - Luna Brendor
My address
My phone
My website : www.lunabrendor.com
my Blog : pebbleandtwig.me

Should not have
• Butterflies, stars, flowers, anything not particularly linked to wine - would like to keep it simple, modern and eye-catching without being too cliche.

```html
<!DOCTYPE html>
<html lang="en">
<head>
<meta charset="utf-8">
<title>Luna Brendor – Business Card</title>
<link href="https://fonts.googleapis.com/css2?family=Jost:wght@300;400&display=swap" rel="stylesheet">
<style>
  :root {
    --backdrop: #a9a9a9;
    --wine-red: #a51a1a;
    --card-white: #ffffff;
    --card-shadow: #7c7a92;
    --name-pink: #f27474;
    --tagline-white: #ffffff;
    --contact-plum: #8b3e4c;
    --art-on-red: #c85a55;
    --art-on-white: #a51a1a;
  }
  * { margin: 0; padding: 0; box-sizing: border-box; }
  html, body {
    width: 1200px;
    height: 404px;
    overflow: hidden;
    background: var(--backdrop);
    font-family: "Jost", "Futura", sans-serif;
    font-weight: 300;
  }
  .stage { position: relative; width: 1200px; height: 404px; }
  .card {
    position: absolute;
    top: 52px;
    height: 285px;
    box-shadow: 9px 9px 0 var(--card-shadow);
  }
  .card--front { left: 78px; width: 486px; background: var(--wine-red); }
  .card--back { left: 648px; width: 479px; background: var(--card-white); }

  .artwork { position: absolute; top: 28px; display: block; }
  .card--front .artwork { left: 17px; width: 115px; height: 222px; }
  .card--back .artwork { left: 17px; width: 112px; height: 222px; }

  .brand {
    position: absolute;
    right: 24px;
    top: 154px;
    text-align: right;
  }
  .brand__name {
    color: var(--name-pink);
    font-size: 37px;
    font-weight: 300;
    letter-spacing: 0.5px;
    line-height: 1;
    text-transform: uppercase;
  }
  .brand__tagline {
    margin-top: 9px;
    color: var(--tagline-white);
    font-size: 17.5px;
    line-height: 26px;
  }

  .contact {
    position: absolute;
    left: 167px;
    top: 73px;
    color: var(--contact-plum);
    font-size: 18.5px;
    line-height: 25px;
    font-style: normal;
  }
  .contact__group + .contact__group { margin-top: 24px; }
</style>
</head>
<body>
<main class="stage">
  <section class="card card--front">
    <svg class="artwork" role="img" aria-label="Sketched wine bottle and wine glass illustration" viewBox="0 0 115 222">
      <rect width="115" height="222" fill="var(--art-on-red)"/>
    </svg>
    <div class="brand">
      <h1 class="brand__name">Luna Brendor</h1>
      <p class="brand__tagline">Communication and Events<br>for the World of Wine</p>
    </div>
  </section>

  <section class="card card--back">
    <svg class="artwork" role="img" aria-label="Sketched wine bottle and wine glass illustration" viewBox="0 0 112 222">
      <rect width="112" height="222" fill="var(--art-on-white)"/>
    </svg>
    <address class="contact">
      <p class="contact__group">Luna Brendor,<br>Lindenhofer Strasse, 36<br>81547 Munich</p>
      <p class="contact__group">Tel: +49 170 5512 384<br>luna@lunabrendor.com</p>
    </address>
  </section>
</main>
</body>
</html>
```